Business Cards for a company that provides webstore services to veterinarians

We need business cards designed for our main service PawCartHub. PawCartHub is a webstore that veterinarian clinics can use to that will allow their clients to purchase products for their pets. Our company is Brindlow Veterinary Solutions (BVS). Our mission statement is We love pets! We will do everything possible to facilitate along, healthy and happy relationship with their families.

Target Market(s)

Veterinarians

Industry/Entity Type

Veterinary

Contact Information for Business Card

I would like the design to incorporate the colours our our company. Cards should have room for employee name, title (only necessary in two instances), phone number, mobile number, email address and linkedin symbol and related profile name ie Marla Quinton. I would like the PawCartHub logo to appear on one side and BVS logo to appear on the other. I will need both an english and french version. I can provide the french translation. Please focus on english version and then we will translate

Colors

Designer to choose colors to be used in the design.

Requirements
Must have
• one side - PawCartHub logo with persons name, phone number, mobile number, email address
• second side - BVS logo
• colours should be consistent with our company. colours are as follows:
• Red
• RGB: 190 / 30 / 45
• CYMK: 14 / 100 / 90 /10
• Hex: #BE1E2D
• Gray
• RGB: 88 / 89 / 86
• CYMK: 3 / 2 / 0 /64
• Hex: #585956
Nice to have
• address of company - can be on either side address is 4817 Feldmoor Street Suite 305 Burlington ON K2R 6T4. Toll free number will vary depending on person
• Linkedin symbol and name of person
• on second side with BVS logo our company's mission statement
Should not have
• nothing comes to mind

```html
<!DOCTYPE html>
<html lang="en">
<head>
<meta charset="utf-8">
<title>PawCartHub / BVS Business Cards</title>
<link rel="stylesheet" href="https://fonts.googleapis.com/css2?family=Roboto+Condensed:wght@400;700&family=Open+Sans:wght@400;600&display=swap">
<style>
  :root {
    --brand-red: #be1e2d;
    --card-red: #cc2433;
    --brand-gray: #585956;
    --paper: #f4f3f1;
    --stage: #e6e6e4;
    --white: #ffffff;
    --rule: #9a9a98;
  }
  * { margin: 0; padding: 0; box-sizing: border-box; }
  html, body { width: 1200px; height: 873px; overflow: hidden; }
  body {
    background: var(--stage);
    position: relative;
    font-family: "Roboto Condensed", Arial, sans-serif;
  }
  .card {
    position: absolute;
    top: 286px;
    width: 520px;
    height: 300px;
    box-shadow: 0 6px 18px rgba(0,0,0,0.18);
  }
  /* Contact side */
  .card--contact { left: 50px; background: var(--paper); }
  .brand-lockup {
    position: absolute;
    top: 52px; left: 0; right: 0;
    display: flex; align-items: center; justify-content: center; gap: 12px;
  }
  .brand-lockup__dot {
    width: 14px; height: 14px; border-radius: 50%;
    background: var(--brand-red);
  }
  .brand-lockup__name {
    font-family: "Open Sans", Arial, sans-serif;
    font-weight: 400;
    font-size: 40px;
    color: var(--brand-gray);
    letter-spacing: -0.5px;
  }
  .divider {
    position: absolute;
    top: 150px; left: 60px; right: 60px; height: 1px;
    background: linear-gradient(90deg, transparent, var(--rule) 20%, var(--rule) 80%, transparent);
  }
  .person {
    position: absolute;
    top: 172px; left: 150px;
  }
  .person__name {
    font-weight: 700;
    font-size: 28px;
    color: var(--brand-red);
    margin-bottom: 8px;
  }
  .contact-list { list-style: none; }
  .contact-list li {
    display: flex; align-items: center; gap: 10px;
    font-size: 18px; line-height: 25px;
    color: var(--brand-gray);
  }
  .contact-list svg { width: 13px; height: 13px; fill: var(--brand-gray); flex: none; }

  /* Company side */
  .card--company { left: 630px; background: var(--card-red); color: var(--white); }
  .company-address {
    position: absolute;
    top: 30px; left: 34px; right: 34px;
    font-weight: 700; font-size: 17px;
  }
  .company-lockup {
    position: absolute;
    top: 128px; left: 0; right: 0;
    display: flex; align-items: center; justify-content: center; gap: 12px;
  }
  .company-lockup__dot {
    width: 14px; height: 14px; border-radius: 50%;
    background: var(--white);
    flex: none;
  }
  .company-lockup__name {
    font-weight: 400;
    font-size: 32px;
    line-height: 1;
  }
  .company-tagline {
    position: absolute;
    top: 178px; left: 0; right: 0;
    text-align: center;
    font-weight: 400;
    font-size: 15px;
    letter-spacing: 1px;
  }
</style>
</head>
<body>
  <section class="card card--contact" aria-label="Contact side">
    <div class="brand-lockup">
      <span class="brand-lockup__dot"></span>
      <span class="brand-lockup__name">pawcarthub.ca</span>
    </div>
    <div class="divider"></div>
    <div class="person">
      <h1 class="person__name">Marla Quinton</h1>
      <ul class="contact-list">
        <li>
          <svg viewBox="0 0 16 16" aria-hidden="true"><path d="M3.6 1.2l2.2 2.9-1.4 1.6c.9 2 2.3 3.5 4.3 4.4l1.6-1.4 2.9 2.2-1.5 2.4C6.6 13.3 2.7 9.4 1.2 3.3z"/></svg>
          555-208-4613
        </li>
        <li>
          <svg viewBox="0 0 16 16" aria-hidden="true"><rect x="4" y="1" width="8" height="14" rx="1.5"/><rect x="5.5" y="3" width="5" height="8" fill="#f4f3f1"/></svg>
          555-208-4670
        </li>
        <li>
          <svg viewBox="0 0 16 16" aria-hidden="true"><rect x="1" y="1" width="14" height="14" rx="2"/></svg>
          /in/MarlaQuinton
        </li>
      </ul>
    </div>
  </section>

  <section class="card card--company" aria-label="Company side">
    <p class="company-address">4817 Feldmoor Street Suite 305 Burlington ON K2R 6T4</p>
    <div class="company-lockup">
      <span class="company-lockup__dot"></span>
      <span class="company-lockup__name">Brindlow Veterinary Solutions</span>
    </div>
    <p class="company-tagline">Caring for every companion</p>
  </section>
</body>
</html>
```